amber crest health and wellness group.

need a full website design , all information provided in word document labeled website blue print

Target Market(s)

first responders, military , people in crisis

Coding

Coded - Design and coding required

Number of Pages Required

1 page

```html
<!DOCTYPE html>
<html lang="en">
<head>
<meta charset="utf-8">
<title>Amber Crest Health &amp; Wellness Group</title>
<link href="https://fonts.googleapis.com/css2?family=Arimo:wght@400;500;600;700&display=swap" rel="stylesheet">
<style>
:root{
  --blue:#1f5a91;
  --blue-dark:#174a7a;
  --ink:#1d1d1f;
  --body:#4a4f57;
  --panel:#d5e0ea;
  --line:#e2e6ea;
  --white:#ffffff;
  --grey-wave:#a7a9ac;
}
*{box-sizing:border-box;margin:0;padding:0}
html,body{width:1200px;height:3221px;overflow:hidden}
body{position:relative;background:var(--white);font-family:"Arimo",Arial,sans-serif;color:var(--ink)}
.abs{position:absolute}
a{color:inherit;text-decoration:none}

/* header */
.site-header{left:0;top:0;width:1200px;height:62px;background:var(--white);z-index:3}
.brand{left:112px;top:14px;display:flex;align-items:center;gap:6px;color:var(--blue);font-weight:700;font-size:12px;letter-spacing:.5px}
.brand .dot{width:12px;height:12px;border-radius:50%;background:var(--blue)}
.nav{left:462px;top:28px;display:flex;gap:34px;font-size:11.5px;color:var(--ink)}
.nav .active{color:var(--blue);font-weight:600;text-decoration:underline;text-underline-offset:4px}
.btn{display:inline-flex;align-items:center;justify-content:center;border-radius:4px;font-weight:700;font-size:11px}
.btn-solid{background:var(--blue);color:var(--white)}
.btn-white{background:var(--white);color:var(--blue)}
.btn-ghost{border:1.5px solid var(--white);color:var(--white)}
.header-cta{left:944px;top:18px;width:144px;height:31px}

/* hero */
.hero{left:0;top:62px;width:1200px;height:582px;overflow:hidden}
.hero-photo{position:absolute;inset:0;background:linear-gradient(90deg,#2a5f93 0%,#5c7fa3 30%,#a9b6c4 55%,#c7ccd2 75%,#bfc6cf 100%)}
.hero-title{left:112px;top:135px;font-size:52px;line-height:58px;font-weight:700;color:var(--white)}
.hero-sub{left:112px;top:258px;font-size:11px;color:var(--white)}
.hero-book{left:112px;top:300px;width:148px;height:32px}
.hero-explore{left:272px;top:300px;width:153px;height:32px}
.hero-wave{left:0;bottom:0;width:1200px;height:170px}

/* section titles */
.section-title{left:0;width:1200px;text-align:center;color:var(--blue);font-weight:700;font-size:32px}
.section-lead{left:250px;width:700px;text-align:center;font-size:11px;line-height:16px;color:var(--body)}

/* service cards */
.service{width:313px;height:295px}
.service .photo{position:absolute;left:0;top:0;width:313px;height:187px;border-radius:3px}
.service .box{position:absolute;left:10px;top:142px;width:293px;height:153px;background:var(--white);border:1px solid var(--line);border-radius:3px;padding:22px 15px 0 15px}
.service h3{font-size:16px;font-weight:600;margin-bottom:10px}
.service p{font-size:10.4px;line-height:14.5px;color:var(--body);height:58px}
.learn{display:flex;align-items:center;gap:4px;color:var(--blue);font-weight:700;font-size:10.5px;margin-top:10px}

/* audience cards */
.aud{width:229px;height:250px;border-radius:3px;overflow:hidden}
.aud .shade{position:absolute;inset:0;background:linear-gradient(180deg,rgba(31,90,145,0) 45%,rgba(31,90,145,.85) 100%)}
.aud h4{position:absolute;left:16px;top:185px;color:var(--white);font-size:16px;font-weight:600}
.aud p{position:absolute;left:16px;top:210px;width:170px;color:var(--white);font-size:10.5px;line-height:13px}
.aud svg{position:absolute;right:14px;bottom:14px}

/* about */
.about{left:112px;top:1911px;width:976px;height:358px;background:var(--blue);border-radius:3px}
.about-photo{left:33px;top:34px;width:436px;height:291px;background:linear-gradient(135deg,#3a3a3d,#8b7866 45%,#d4cbc0 70%,#2e2e31);border-radius:2px}
.about-text{left:510px;top:40px;width:420px;color:var(--white)}
.about-text h2{font-size:32px;font-weight:700;margin-bottom:12px}
.about-text p{font-size:10.4px;line-height:15.7px;margin-bottom:4px}
.about-btn{margin-top:12px;width:98px;height:30px}

.mv{top:2289px;width:478px;height:224px;background:var(--panel);border-radius:2px}
.mv .circle{position:absolute;left:30px;top:35px;width:156px;height:156px;border-radius:50%}
.mv .text{position:absolute;left:222px;top:36px;width:225px}
.mv h3{display:flex;align-items:center;gap:7px;color:var(--blue);font-size:20px;font-weight:600;margin-bottom:10px}
.mv p{font-size:10.4px;line-height:15.6px;color:var(--body)}

/* partners */
.partners{left:112px;top:2626px;width:976px;height:90px}
.partner{position:absolute;background:#c9d3dd}
.dots{left:544px;top:2720px;display:flex;gap:5px}
.dots span{width:9px;height:9px;border-radius:50%;background:#cfd6dd}
.dots .on{background:var(--blue)}

/* footer */
.footer-wave{left:0;top:2760px;width:1200px;height:80px}
.footer{left:0;top:2839px;width:1200px;height:382px;background:var(--blue);color:var(--white)}
.cta-title{left:206px;top:70px;font-size:29px;font-weight:600}
.cta-btn{left:896px;top:72px;width:99px;height:29px}
.rule{left:112px;top:122px;width:976px;height:1px;background:rgba(255,255,255,.55)}
.f-brand{left:115px;top:170px;display:flex;align-items:center;gap:8px;font-weight:700;font-size:17px;letter-spacing:.5px}
.f-brand .dot{width:16px;height:16px;border-radius:50%;background:var(--white)}
.socials{left:112px;top:271px;display:flex;gap:7px}
.socials span{width:24px;height:24px;border-radius:3px;background:var(--white)}
.f-col h4{font-size:17px;font-weight:600;margin-bottom:14px}
.f-col li{list-style:none;font-size:11px;line-height:20.6px}
.f-contact li{display:flex;gap:7px;align-items:flex-start;margin-bottom:14px;line-height:14px}
.rule2{left:274px;top:330px;width:652px;height:1px;background:rgba(255,255,255,.55)}
.copy{left:0;top:349px;width:1200px;text-align:center;font-size:10.5px}
</style>
</head>
<body>

<header class="site-header abs">
  <div class="brand abs"><span class="dot"></span>AMBER CREST</div>
  <nav class="nav abs">
    <a class="active">Home</a><a>About Us</a><a>Our Services &#8964;</a><a>Our Team</a><a>FAQ</a><a>Contact Us</a>
  </nav>
  <a class="btn btn-solid header-cta abs">Schedule a Session</a>
</header>

<section class="hero abs">
  <div class="hero-photo" role="img" aria-label="Woman with curly hair covering her face in distress, with a counsellor beside her"></div>
  <h1 class="hero-title abs">Helping Those<br>Who Help Others</h1>
  <p class="hero-sub abs">Trauma-informed mental health and integrative wellness care in St. Catharines.</p>
  <a class="btn btn-white hero-book abs">Book a Consultation</a>
  <a class="btn btn-ghost hero-explore abs">Explore Our Services</a>
  <svg class="hero-wave abs" viewBox="0 0 1200 170" preserveAspectRatio="none">
    <path d="M0,170 L0,130 C250,60 480,58 700,110 C860,150 1020,115 1200,80 L1200,170 Z" fill="#ffffff"/>
    <path d="M0,118 C250,40 500,50 700,95 C880,135 1040,70 1200,30 L1200,80 C1020,115 860,150 700,110 C480,58 250,60 0,130 Z" fill="#1f5a91"/>
  </svg>
</section>

<h2 class="section-title abs" style="top:674px">Our Services</h2>
<p class="section-lead abs" style="top:718px">We provide trauma-informed therapy and holistic wellness services for first responders, clinicians, and the community. From mental health support to advanced wellness therapies, our team helps clients heal, recover, and thrive.</p>

<article class="service abs" style="left:112px;top:769px">
  <div class="photo" role="img" aria-label="Firefighter in turnout gear sitting exhausted" style="background:linear-gradient(135deg,#e6e4e1,#8a6a3e 55%,#c9c4bc)"></div>
  <div class="box"><h3>Trauma &amp; First Responder</h3><p>Specialized programs designed for police, fire, EMS, corrections, and frontline workers. Focused on resilience, recovery, and navigating high-stress environments.</p><a class="learn">Learn More <svg width="16" height="8" viewBox="0 0 16 8"><path d="M0 4H14M11 1L14.5 4L11 7" stroke="#1f5a91" stroke-width="1.3" fill="none"/></svg></a></div>
</article>
<article class="service abs" style="left:444px;top:769px">
  <div class="photo" role="img" aria-label="Woman on a couch talking with a therapist in a bright office" style="background:linear-gradient(135deg,#f1f0ee,#c8c5bf 50%,#7f8f6a)"></div>
  <div class="box"><h3>Mental Health Therapy</h3><p>Evidence-based counselling for adults, teens, and first responders. We support anxiety, depression, trauma, stress, and personal growth through individualized care.</p><a class="learn">Learn More <svg width="16" height="8" viewBox="0 0 16 8"><path d="M0 4H14M11 1L14.5 4L11 7" stroke="#1f5a91" stroke-width="1.3" fill="none"/></svg></a></div>
</article>
<article class="service abs" style="left:775px;top:769px">
  <div class="photo" role="img" aria-label="Physiotherapist guiding a patient through arm stretches" style="background:linear-gradient(135deg,#f2f1ef,#d9d3cc 50%,#8fb7d6)"></div>
  <div class="box"><h3>Physiotherapy</h3><p>Personalized treatment to reduce pain, restore mobility, and rebuild strength through evidence-based exercise, manual therapy, and functional movement support.</p><a class="learn">Learn More <svg width="16" height="8" viewBox="0 0 16 8"><path d="M0 4H14M11 1L14.5 4L11 7" stroke="#1f5a91" stroke-width="1.3" fill="none"/></svg></a></div>
</article>

<article class="service abs" style="left:112px;top:1083px">
  <div class="photo" role="img" aria-label="Support group session with a counsellor comforting a man" style="background:linear-gradient(135deg,#d8d6d3,#5b5650 50%,#8d8276)"></div>
  <div class="box"><h3>Trauma-Informed Approach</h3><p>All interventions are delivered with sensitivity, respecting individual experiences, cultural backgrounds, and personal boundaries to foster safety and trust.</p><a class="learn">Learn More <svg width="16" height="8" viewBox="0 0 16 8"><path d="M0 4H14M11 1L14.5 4L11 7" stroke="#1f5a91" stroke-width="1.3" fill="none"/></svg></a></div>
</article>
<article class="service abs" style="left:444px;top:1083px">
  <div class="photo" role="img" aria-label="Two women embracing in a supportive hug outdoors" style="background:linear-gradient(135deg,#a9b98f,#c7b99f 50%,#6f7d5a)"></div>
  <div class="box"><h3>Immediate Emotional Support</h3><p>We provide prompt, compassionate support for individuals experiencing acute stress, shock, or overwhelming emotions following a traumatic event.</p><a class="learn">Learn More <svg width="16" height="8" viewBox="0 0 16 8"><path d="M0 4H14M11 1L14.5 4L11 7" stroke="#1f5a91" stroke-width="1.3" fill="none"/></svg></a></div>
</article>
<article class="service abs" style="left:775px;top:1083px">
  <div class="photo" role="img" aria-label="Young woman standing amid disaster debris" style="background:linear-gradient(135deg,#4f5a66,#8b8a80 50%,#3e4750)"></div>
  <div class="box"><h3>Crisis &amp; Critical Incident</h3><p>Immediate support for first responders and professionals following traumatic events. Our clinicians offer safe, structured debriefing to reduce long-term impact.</p><a class="learn">Learn More <svg width="16" height="8" viewBox="0 0 16 8"><path d="M0 4H14M11 1L14.5 4L11 7" stroke="#1f5a91" stroke-width="1.3" fill="none"/></svg></a></div>
</article>

<a class="btn btn-solid abs" style="left:535px;top:1402px;width:130px;height:32px">View All Services</a>

<h2 class="section-title abs" style="top:1488px">Who We Serve</h2>

<article class="aud abs" style="left:112px;top:1543px">
  <div style="position:absolute;inset:0;background:linear-gradient(160deg,#c9ccc6,#8a7457 55%,#6c6a60)" role="img" aria-label="Firefighter in helmet and gear"></div>
  <div class="shade"></div>
  <h4>First Responders</h4><p>Support for trauma, stress, and mental wellness</p>
  <svg width="16" height="8" viewBox="0 0 16 8"><path d="M0 4H14M11 1L14.5 4L11 7" stroke="#fff" stroke-width="1.3" fill="none"/></svg>
</article>
<article class="aud abs" style="left:360px;top:1543px">
  <div style="position:absolute;inset:0;background:linear-gradient(160deg,#7fae4f,#3d6fae 45%,#c9b39a)" role="img" aria-label="Smiling teenagers posing together outdoors"></div>
  <div class="shade"></div>
  <h4>Adults &amp; Teens</h4><p>Individualized therapy and holistic care</p>
  <svg width="16" height="8" viewBox="0 0 16 8"><path d="M0 4H14M11 1L14.5 4L11 7" stroke="#fff" stroke-width="1.3" fill="none"/></svg>
</article>
<article class="aud abs" style="left:608px;top:1543px">
  <div style="position:absolute;inset:0;background:linear-gradient(160deg,#cfd3d3,#7a7560 50%,#4c4d45)" role="img" aria-label="Soldier in combat gear and helmet"></div>
  <div class="shade"></div>
  <h4>Military</h4><p>Care tailored for those who serve and have served</p>
  <svg width="16" height="8" viewBox="0 0 16 8"><path d="M0 4H14M11 1L14.5 4L11 7" stroke="#fff" stroke-width="1.3" fill="none"/></svg>
</article>
<article class="aud abs" style="left:857px;top:1543px">
  <div style="position:absolute;inset:0;background:linear-gradient(160deg,#9fb4c8,#b88d6f 50%,#e2ddd7)" role="img" aria-label="Stressed woman resting her head on her hand at a desk"></div>
  <div class="shade"></div>
  <h4>People in Crisis</h4><p>Professional support, supervision, and wellness programs</p>
  <svg width="16" height="8" viewBox="0 0 16 8"><path d="M0 4H14M11 1L14.5 4L11 7" stroke="#fff" stroke-width="1.3" fill="none"/></svg>
</article>

<a class="btn btn-solid abs" style="left:552px;top:1818px;width:96px;height:31px">View More</a>

<section class="about abs">
  <div class="about-photo abs" role="img" aria-label="Grieving woman holding a tissue while a counsellor holds her hand"></div>
  <div class="about-text abs">
    <h2>About Us</h2>
    <p>Amber Crest Health &amp; Wellness Group was created to provide a safe, supportive space for those who give so much to others. With a trauma-informed approach at the core of our philosophy, we offer a blend of clinical mental health services and innovative wellness therapies designed to support the whole person—mind, body, and nervous system.</p>
    <p>Our multidisciplinary team includes experienced therapists, clinicians, and wellness practitioners who work collaboratively to ensure every client receives personalized, evidence-based care. We are committed to serving first responders, healthcare professionals, families, and individuals seeking meaningful, sustainable healing.</p>
    <p>Here, clients are met with compassion, professionalism, and a deep respect for their lived experiences.</p>
    <a class="btn btn-white about-btn">Learn More</a>
  </div>
</section>

<article class="mv abs" style="left:112px">
  <div class="circle" role="img" aria-label="Team members stacking hands together over a desk" style="background:linear-gradient(135deg,#c46a4a,#e9e2da 50%,#6d5a4a)"></div>
  <div class="text">
    <h3><svg width="18" height="18" viewBox="0 0 18 18"><circle cx="9" cy="9" r="7.5" stroke="#1f5a91" stroke-width="1.8" fill="none"/><circle cx="9" cy="9" r="4" stroke="#1f5a91" stroke-width="1.8" fill="none"/><circle cx="9" cy="9" r="1.4" fill="#1f5a91"/></svg>Mission</h3>
    <p>Our mission is to provide trauma-informed, evidence-based mental health and wellness services that support healing, recovery, and resilience. We are committed to offering accessible, confidential care tailored to the unique needs of first responders, healthcare professionals, and individuals facing stress and trauma.</p>
  </div>
</article>
<article class="mv abs" style="left:609px">
  <div class="circle" role="img" aria-label="Business presenter in front of a vision board" style="background:linear-gradient(135deg,#f1c437,#dfe6ee 50%,#2c3b57)"></div>
  <div class="text">
    <h3><svg width="20" height="14" viewBox="0 0 20 14"><path d="M1 7C4 2 16 2 19 7C16 12 4 12 1 7Z" stroke="#1f5a91" stroke-width="1.8" fill="none"/><circle cx="10" cy="7" r="2.6" fill="#1f5a91"/></svg>Vision</h3>
    <p>Our vision is to redefine wellness by bringing together mental health therapy, trauma recovery, and integrative body-based treatments under one roof. We aim to create a calm and supportive environment where individuals can rebuild their emotional, physical, and psychological strength with confidence and dignity.</p>
  </div>
</article>

<h2 class="section-title abs" style="top:2568px">Our Community Partners</h2>
<div class="partners abs">
  <div class="partner" style="left:52px;top:30px;width:130px;height:30px;border-radius:4px"></div>
  <div class="partner" style="left:255px;top:34px;width:110px;height:22px;border-radius:4px"></div>
  <div class="partner" style="left:438px;top:33px;width:104px;height:24px;border-radius:4px"></div>
  <div class="partner" style="left:617px;top:4px;width:82px;height:82px;border-radius:50%"></div>
  <div class="partner" style="left:772px;top:29px;width:158px;height:32px;border-radius:4px"></div>
</div>
<div class="dots abs"><span></span><span></span><span class="on"></span><span></span><span></span><span></span><span></span><span></span></div>

<svg class="footer-wave abs" viewBox="0 0 1200 80" preserveAspectRatio="none">
  <path d="M0,50 C250,-10 500,30 700,55 C900,78 1080,40 1200,20 L1200,80 L0,80 Z" fill="#a7a9ac"/>
  <path d="M0,70 C260,20 500,45 720,70 C900,85 1080,55 1200,35 L1200,80 L0,80 Z" fill="#1f5a91"/>
</svg>

<footer class="footer abs">
  <h2 class="cta-title abs">Ready to Begin Your Healing Journey?</h2>
  <a class="btn btn-white cta-btn abs">Contact Us</a>
  <div class="rule abs"></div>

  <div class="f-brand abs"><span class="dot"></span>AMBER CREST</div>
  <div class="socials abs"><span></span><span></span><span></span><span></span></div>

  <div class="f-col abs" style="left:354px;top:160px">
    <h4>Quick Links</h4>
    <ul><li>Home</li><li>About Us</li><li>Mission &amp; Vision</li><li>Who We Serve</li><li>Privacy Policy</li><li>Tems &amp; Condition</li></ul>
  </div>
  <div class="f-col abs" style="left:582px;top:160px">
    <h4>Our Services</h4>
    <ul><li>Trauma &amp; First Responder</li><li>Mental health Therapy</li><li>Physiotherapy</li><li>Trauma-Informed Approach</li><li>Immediate Emotional Support</li><li>Crisis &amp; Critical Incident</li></ul>
  </div>
  <div class="f-col f-contact abs" style="left:854px;top:160px">
    <h4>Contact Information</h4>
    <ul>
      <li><svg width="11" height="13" viewBox="0 0 11 13"><path d="M5.5 12C5.5 12 1 7.5 1 5A4.5 4.5 0 0 1 10 5C10 7.5 5.5 12 5.5 12Z" stroke="#fff" fill="none"/><circle cx="5.5" cy="5" r="1.5" stroke="#fff" fill="none"/></svg><span>123 Placeholder Address,<br>St. Catharines, Ontario</span></li>
      <li><svg width="12" height="12" viewBox="0 0 12 12"><path d="M2 1L4.5 1L5.5 4L4 5C4.8 6.8 5.2 7.2 7 8L8 6.5L11 7.5L11 10C6 11 1 6 2 1Z" stroke="#fff" fill="none"/></svg><span>+1234567890</span></li>
      <li><svg width="12" height="10" viewBox="0 0 12 10"><rect x=".5" y=".5" width="11" height="9" stroke="#fff" fill="none"/><path d="M.5 .5L6 5.5L11.5 .5" stroke="#fff" fill="none"/></svg><span>info@ambercrestwellness.ca</span></li>
    </ul>
  </div>
  <div class="rule2 abs"></div>
  <p class="copy abs">© 2026 Amber Crest Health &amp; Wellness Group. All Rights Reserved.</p>
</footer>

</body>
</html>
```